I need a business card for my original fine art pieces

I would like a business card design including a logo design for a new business in the art world. I am based in the Hunter Valley NSW Australia. I am a contemporary figurative, encaustic and wildlife artist. I would like to be able to upload my email and mobile number to this as well. This design should be one that I can incorporate into banners and flyers etc. Id like to incorporate one of my own images or partial image into the background or somewhere below. My initials are KD and I would like these used as a logo type. I would like the use of some colour and it to be bright and catchy. The final design should communicate artwork custom made and commissions available.

Overview: Original Fine Artworks for sale, online, art galleries etc, Custom made to order and by commission.

Target market is world wide audience and corporate world

My figurative work is painted using acrylics in a lot of natural ochre colours that reflect the Australian Outback, on canvas, linen, paper or board: My encaustic work is created in a contemporary abstract style using a blow torch and a made with a medium of 100% pure bees wax, Damar resin, mixed media and coloured pigments, applied to Birch board. My wildlife are created using coloured pencil and mixed media on a variety of paper types or board.

```html
<!DOCTYPE html>
<html lang="en">
<head>
<meta charset="utf-8">
<title>Kara Dunmore – Business Card</title>
<link href="https://fonts.googleapis.com/css2?family=Montserrat:wght@800&family=Arimo:wght@400&display=swap" rel="stylesheet">
<style>
  :root {
    --stage: #d9d9d9;
    --card: #050505;
    --card-edge: #151515;
    --red: #e01e0e;
    --white: #ffffff;
    --muted: #f2f2f2;
  }
  * { box-sizing: border-box; margin: 0; padding: 0; }
  html, body { width: 1200px; height: 1200px; overflow: hidden; }
  body {
    background: var(--stage);
    display: flex;
    flex-direction: column;
    align-items: center;
    justify-content: center;
    gap: 60px;
  }
  .card {
    position: relative;
    width: 900px;
    height: 510px;
    background: radial-gradient(ellipse at 55% 40%, var(--card-edge), var(--card) 70%);
    overflow: hidden;
    box-shadow: 0 6px 18px rgba(0,0,0,0.25);
  }

  /* Plain name mark shared by both sides */
  .namemark {
    font-family: "Arimo", sans-serif;
    font-weight: 400;
    color: var(--red);
    white-space: nowrap;
    letter-spacing: 0.04em;
  }

  /* Back side */
  .card--back { display: flex; align-items: center; justify-content: center; }
  .card--back .namemark { font-size: 52px; }

  /* Front side */
  .front__title { position: absolute; left: 70px; top: 50px; }
  .front__name {
    font-family: "Montserrat", sans-serif;
    font-weight: 800;
    font-size: 40px;
    color: var(--red);
    letter-spacing: 0.01em;
  }
  .front__role {
    font-family: "Arimo", sans-serif;
    font-size: 19px;
    color: var(--white);
    margin-top: 4px;
    letter-spacing: 0.02em;
  }
  .front__namemark { position: absolute; left: 40px; top: 295px; font-size: 30px; }

  .front__divider {
    position: absolute;
    left: 395px;
    top: 245px;
    width: 1px;
    height: 150px;
    background: var(--red);
  }
  .contact {
    position: absolute;
    left: 425px;
    top: 248px;
    list-style: none;
    font-family: "Arimo", sans-serif;
    font-size: 21px;
    color: var(--muted);
    line-height: 1.55;
  }
  .contact__label { color: var(--red); display: inline-block; width: 30px; }

  .front__bands { position: absolute; left: 0; bottom: 0; width: 900px; height: 90px; }
</style>
</head>
<body>

  <section class="card card--back" aria-label="Card back">
    <span class="namemark">KARA DUNMORE</span>
  </section>

  <section class="card card--front" aria-label="Card front">
    <header class="front__title">
      <h1 class="front__name">KARA DUNMORE</h1>
      <p class="front__role">Figurative, Encaustic &amp; Wildlife Artist</p>
    </header>

    <span class="namemark front__namemark">KARA DUNMORE</span>

    <span class="front__divider" aria-hidden="true"></span>

    <ul class="contact">
      <li><span class="contact__label">M:</span>1-555-010270</li>
      <li><span class="contact__label"></span>Clearwater Valley, NSW Australia</li>
      <li><span class="contact__label">W:</span>www.karadunmorefineart.com</li>
      <li><span class="contact__label">E:</span>hello@karadunmorefineart.com</li>
    </ul>

    <svg class="front__bands" viewBox="0 0 900 90" aria-hidden="true">
      <polygon points="0,30 505,90 0,90" fill="var(--red)"/>
      <polygon points="520,30 900,30 900,90 530,90" fill="var(--white)"/>
    </svg>
  </section>

</body>
</html>
```